Coffee, Bar , Bakery, Wine Bar, Business based in Fort Lauderdale FL.
We need Logo Design Website (PC and Mobile) design with order and pickup online managment service. Cold Colors Main Images will be glass or bottle of wine and coffee related images
I Attach a logo we found online and we like something like that.

Industry/Entity Type

Business

Logo Text

MERIDO Coffee & Food Co

Number of Pages Required

4 page

Requirements
Must have
• Order online for in store pickup. MENU PAGE !!
Nice to have
• Map with address , link to all social , option to add daily pictures in a slide.
Should not have
• not many white spaces on the web page.

```html
<!DOCTYPE html>
<html lang="en">
<head>
<meta charset="utf-8">
<title>Merido Bar &amp; Bakery</title>
<link rel="stylesheet" href="https://fonts.googleapis.com/css2?family=Dancing+Script:wght@500;700&family=Montserrat:wght@400;500;600&family=Open+Sans:wght@400;600&display=swap">
<style>
:root{
  --maroon:#7e2a1f;
  --maroon-deep:#832a20;
  --ink:#1d1d1d;
  --text:#444;
  --muted:#8a8a8a;
  --line:#e6e6e6;
  --white:#fff;
}
*{margin:0;padding:0;box-sizing:border-box}
html,body{width:1200px;height:2667px;overflow:hidden;background:var(--white)}
body{position:relative;font-family:"Open Sans",Arial,sans-serif;color:var(--text)}
.abs{position:absolute}
.script{font-family:"Dancing Script",cursive;font-weight:500}

/* header */
.site-header{left:0;top:0;width:1200px;height:137px;background:var(--white)}
.brand{left:101px;top:28px;display:flex;align-items:center;gap:14px}
.brand-mark{width:78px;height:78px;border-radius:50%;background:var(--maroon)}
.brand-name{font-family:"Montserrat",sans-serif;font-weight:600;font-size:20px;color:var(--maroon)}
.main-nav{top:60px;left:0;width:1200px}
.main-nav a{position:absolute;font-family:"Montserrat",sans-serif;font-size:16px;color:var(--ink);text-decoration:none;white-space:nowrap}
.main-nav a.active{color:var(--maroon)}
.main-nav a.active::after{content:"";position:absolute;left:-6px;right:-6px;top:32px;height:2px;background:var(--maroon)}

/* hero */
.hero{left:0;top:137px;width:1200px;height:620px;overflow:hidden}
.hero-photo{position:absolute;inset:0;background:linear-gradient(180deg,#5b4236 0%,#3a2c26 55%,#1f1a18 100%)}
.hero-title{position:absolute;left:0;width:1200px;top:190px;text-align:center;font-size:64px;color:var(--white);text-shadow:0 2px 6px rgba(0,0,0,.35)}
.hero-arrow{position:absolute;top:225px}
.hero-curve{position:absolute;left:0;bottom:0}

/* welcome */
.welcome-title{left:0;width:1200px;top:800px;text-align:center;font-size:38px;color:var(--ink)}
.welcome-title em{font-style:normal;color:var(--maroon)}
.welcome-text{left:135px;width:930px;top:860px;text-align:center;font-size:13.5px;line-height:28px;color:var(--muted)}
.welcome-rule{left:220px;width:760px;top:958px;height:1px;background:var(--line)}

.feature{top:990px;width:262px;text-align:center}
.feature-icon{width:131px;height:131px;border-radius:50%;border:3px solid var(--maroon);margin:0 auto;padding:5px}
.feature-icon span{display:flex;width:100%;height:100%;border-radius:50%;background:var(--maroon);align-items:center;justify-content:center}
.feature h3{font-family:"Montserrat",sans-serif;font-weight:400;font-size:19px;color:var(--ink);margin-top:16px;letter-spacing:.5px}
.feature p{font-size:13.5px;line-height:21px;color:#666;margin:8px 20px 0}
.btn-outline{display:inline-block;margin-top:18px;width:153px;height:43px;line-height:41px;border:1.5px solid var(--maroon);color:var(--maroon);font-family:"Montserrat",sans-serif;font-size:15px;text-decoration:none}

/* promo band */
.promo{left:0;top:1362px;width:1200px;height:411px;overflow:hidden}
.promo-photo{position:absolute;inset:0;background:linear-gradient(100deg,#8a4a35 0%,#a0553c 50%,#7a3a2a 100%)}
.promo-title{position:absolute;left:0;width:1200px;top:34px;text-align:center;font-size:66px;color:var(--white)}
.promo-text{position:absolute;left:160px;width:880px;top:128px;text-align:center;font-family:"Montserrat",sans-serif;font-size:19.5px;line-height:35.5px;color:#f5ebe6}
.btn-ghost{position:absolute;left:466px;top:297px;width:270px;height:50px;line-height:48px;border:1.5px solid rgba(255,255,255,.85);text-align:center;color:var(--white);font-family:"Montserrat",sans-serif;font-weight:600;font-size:18px;letter-spacing:1px;text-decoration:none}

/* services */
.services-title{left:0;width:1200px;top:1812px;text-align:center;font-size:38px;color:var(--ink)}
.services-title em{font-style:normal;color:var(--maroon)}
.carousel-btn{top:1826px;width:27px;height:27px;border-radius:50%;background:#e3e3e3;display:flex;align-items:center;justify-content:center}
.service-card{top:1899px;width:313px}
.service-photo{height:183px}
.service-card h3{font-family:"Montserrat",sans-serif;font-weight:400;font-size:19.5px;color:var(--ink);margin-top:24px;letter-spacing:.5px;white-space:nowrap}
.service-card p{font-size:13.5px;line-height:21px;color:#888;margin-top:12px;padding-right:10px}
.btn-solid{display:inline-flex;align-items:center;gap:8px;margin-top:36px;height:40px;padding:0 20px;background:var(--maroon);color:var(--white);font-family:"Montserrat",sans-serif;font-size:15px;text-decoration:none}

/* footer */
.site-footer{left:0;top:2338px;width:1200px;height:329px;background:var(--maroon-deep);color:#f1e4e0}
.footer-col{position:absolute;top:44px;height:195px;border-right:1px solid rgba(255,255,255,.08)}
.footer-col h4{font-family:"Dancing Script",cursive;font-weight:500;font-size:21px;color:var(--white);text-transform:uppercase;white-space:nowrap}
.footer-col ul{list-style:none;margin-top:12px}
.footer-col li{font-size:13.5px;line-height:30px;color:#f1e4e0;display:flex;align-items:center;gap:12px;white-space:nowrap}
.footer-col p{font-size:13.5px;margin-top:14px;white-space:nowrap}
.social{display:flex;gap:6px;margin-top:16px}
.social span{width:36px;height:36px;border-radius:50%;border:2px solid #fff}
.footer-rule{position:absolute;left:101px;width:999px;top:260px;height:1px;background:rgba(255,255,255,.35)}
.copyright{position:absolute;left:101px;top:282px;font-size:12.5px;color:#f1e4e0}
</style>
</head>
<body>

<header class="site-header abs">
  <div class="brand abs">
    <span class="brand-mark"></span>
    <span class="brand-name">Merido Bar &amp; Bakery</span>
  </div>
  <nav class="main-nav abs">
    <a class="active" style="left:516px">Home</a>
    <a style="left:608px">About Us</a>
    <a style="left:727px">Services</a>
    <a style="left:836px">Blog</a>
    <a style="left:916px">Menus</a>
    <a style="left:1011px">Contact Us</a>
  </nav>
</header>

<section class="hero abs">
  <div class="hero-photo" role="img" aria-label="Photo: cake and coffee cup on a café table"></div>
  <h1 class="hero-title script">We are offering in Bar &amp; Bakery</h1>
  <svg class="hero-arrow" style="left:30px" width="20" height="36" viewBox="0 0 20 36"><path d="M17 2 3 18l14 16" fill="none" stroke="rgba(255,255,255,.7)" stroke-width="2"/></svg>
  <svg class="hero-arrow" style="left:1142px" width="20" height="36" viewBox="0 0 20 36"><path d="M3 2l14 16L3 34" fill="none" stroke="rgba(255,255,255,.7)" stroke-width="2"/></svg>
  <svg class="hero-curve" width="1200" height="60" viewBox="0 0 1200 60" preserveAspectRatio="none"><path d="M0 0Q600 75 1200 0V60H0Z" fill="#fff"/></svg>
</section>

<h2 class="welcome-title abs script">WELCOME TO <em>MERIDO BAR &amp; BAKERY</em></h2>
<p class="welcome-text abs">Sed ut perspiciatis unde omnis iste natus error sit voluptatem accusantium doloremque laudantium, totam rem aperiam, eaque ipsa quae ab illo inventore veritatis et quasi architecto beatae vitae dicta sunt explicabo. Nemo enim ipsam voluptatem quia voluptas sit aspernatur aut odit aut fugit, sed quia consequuntur magni dolores eos qui ratione voluptatem sequi nesciunt.</p>
<div class="welcome-rule abs"></div>

<article class="feature abs" style="left:73px">
  <div class="feature-icon"><span>
    <svg width="60" height="60" viewBox="0 0 60 60" fill="#fff"><path d="M10 38a20 20 0 0 1 40 0z"/><rect x="6" y="40" width="48" height="4" rx="2"/><circle cx="30" cy="16" r="3"/></svg>
  </span></div>
  <h3>BAR</h3>
  <p>Praesent vestibulum aenean nonummy endrerit mauris. Cum sociis natoque..</p>
  <a class="btn-outline">READ MORE</a>
</article>
<article class="feature abs" style="left:335px">
  <div class="feature-icon"><span>
    <svg width="60" height="60" viewBox="0 0 60 60" fill="#fff"><path d="M8 26a22 14 0 0 1 44 0z"/><rect x="6" y="29" width="48" height="5" rx="2"/><rect x="8" y="36" width="44" height="10" rx="4"/></svg>
  </span></div>
  <h3>BAKERY</h3>
  <p>Praesent vestibulum aenean nonummy endrerit mauris. Cum sociis natoque..</p>
  <a class="btn-outline">READ MORE</a>
</article>
<article class="feature abs" style="left:603px">
  <div class="feature-icon"><span>
    <svg width="60" height="60" viewBox="0 0 60 60" fill="none" stroke="#fff" stroke-width="3"><path d="M20 8h20c0 14-3 22-10 22S20 22 20 8z"/><path d="M30 30v20M22 52h16"/><path d="M21 18h18" stroke-width="2"/></svg>
  </span></div>
  <h3>WINE BAR</h3>
  <p>Praesent vestibulum aenean nonummy endrerit mauris. Cum sociis natoque..</p>
  <a class="btn-outline">READ MORE</a>
</article>
<article class="feature abs" style="left:865px">
  <div class="feature-icon"><span>
    <svg width="60" height="60" viewBox="0 0 60 60"><path d="M24 8c-4 4 4 6 0 10M32 8c-4 4 4 6 0 10" fill="none" stroke="#fff" stroke-width="2.5"/><rect x="12" y="26" width="36" height="10" rx="4" fill="#fff"/><path d="M6 40h48l-6 8H12z" fill="#fff"/></svg>
  </span></div>
  <h3>BUSINESS</h3>
  <p>Praesent vestibulum aenean nonummy endrerit mauris. Cum sociis natoque..</p>
  <a class="btn-outline">READ MORE</a>
</article>

<section class="promo abs">
  <div class="promo-photo" role="img" aria-label="Photo: glass of wine in warm bar light"></div>
  <h2 class="promo-title script">Merido Bar &amp; Bakery</h2>
  <p class="promo-text">Donec sodales sagittis magna. Sed consequat, leo eget bibendum sodales. There are many variations of passages of Lorem Ipsum available, but the majority have suffered alteration in some form, by injected humour, or randomised words which don't look even slightly believable.</p>
  <a class="btn-ghost">ORDER NOW !</a>
</section>

<h2 class="services-title abs script">OUR <em>SERVICES</em></h2>
<div class="carousel-btn abs" style="left:1041px"><svg width="8" height="10" viewBox="0 0 8 10"><path d="M6 1 2 5l4 4" fill="none" stroke="#555" stroke-width="1.5"/></svg></div>
<div class="carousel-btn abs" style="left:1073px"><svg width="8" height="10" viewBox="0 0 8 10"><path d="M2 1l4 4-4 4" fill="none" stroke="#555" stroke-width="1.5"/></svg></div>

<article class="service-card abs" style="left:101px">
  <div class="service-photo" role="img" aria-label="Photo: glasses of red and white wine" style="background:linear-gradient(135deg,#cfc7a8 0%,#a88a6a 100%)"></div>
  <h3>NISI UT ALIQUIP EX EA</h3>
  <p>Ut enim ad minim veniam, quis nostrud exercitation ullamco laboris nisi ut aliquip ex ea commodo...</p>
  <a class="btn-solid">View More <svg width="7" height="10" viewBox="0 0 7 10"><path d="M1 1l4 4-4 4" fill="none" stroke="#fff" stroke-width="1.5"/></svg></a>
</article>
<article class="service-card abs" style="left:443px">
  <div class="service-photo" role="img" aria-label="Photo: coffee and pastries at a café table" style="background:linear-gradient(135deg,#c4a079 0%,#8d6a4d 100%)"></div>
  <h3>BEATAE VITAE DICTA SUNT</h3>
  <p>Lorem ipsum dolor sit amet, consectetur adipiscing elit, sed do eiusmod tempor incididunt ut labore...</p>
  <a class="btn-solid">View More <svg width="7" height="10" viewBox="0 0 7 10"><path d="M1 1l4 4-4 4" fill="none" stroke="#fff" stroke-width="1.5"/></svg></a>
</article>
<article class="service-card abs" style="left:788px">
  <div class="service-photo" role="img" aria-label="Photo: cup of coffee with roasted beans" style="background:linear-gradient(135deg,#6e4a33 0%,#3d2416 100%)"></div>
  <h3>MAGNAM ALIQUAM QUAERAT</h3>
  <p>Excepteur sint occaecat cupidatat non proident, sunt in culpa qui officia deserunt mollit anim id est laborum...</p>
  <a class="btn-solid">View More <svg width="7" height="10" viewBox="0 0 7 10"><path d="M1 1l4 4-4 4" fill="none" stroke="#fff" stroke-width="1.5"/></svg></a>
</article>

<footer class="site-footer abs">
  <div class="footer-col" style="left:101px;width:145px">
    <h4>Quick Links</h4>
    <ul><li>Home</li><li>About Us</li><li>Blog</li><li>Menus</li><li>Contact Us</li></ul>
  </div>
  <div class="footer-col" style="left:292px;width:170px">
    <h4>Services</h4>
    <ul><li>Bar</li><li>Bakery</li><li>Wine bar</li><li>Business</li><li>Others</li></ul>
  </div>
  <div class="footer-col" style="left:507px;width:220px">
    <h4>Get in Touch</h4>
    <ul>
      <li><svg width="13" height="13" viewBox="0 0 24 24" fill="#fff"><path d="M6.6 10.8a15 15 0 0 0 6.6 6.6l2.2-2.2a1 1 0 0 1 1-.25 11.4 11.4 0 0 0 3.6.57 1 1 0 0 1 1 1V20a1 1 0 0 1-1 1A17 17 0 0 1 3 4a1 1 0 0 1 1-1h3.5a1 1 0 0 1 1 1c0 1.25.2 2.45.57 3.57a1 1 0 0 1-.25 1z"/></svg>Call us on (01) 48209137</li>
      <li><svg width="13" height="11" viewBox="0 0 24 20" fill="#fff"><path d="M0 2h24v2L12 11 0 4zM0 7l12 7 12-7v13H0z"/></svg>hello@meridobakery.com</li>
    </ul>
  </div>
  <div class="footer-col" style="left:768px;width:118px">
    <h4>Why Us</h4>
    <ul><li>Customers</li><li>Team</li><li>FAQ</li><li>Contact</li></ul>
  </div>
  <div class="footer-col" style="left:926px;width:180px;border-right:none">
    <h4>Follow Us</h4>
    <p>Please connect with us on</p>
    <div class="social">
      <span style="background:#3aa3da"></span>
      <span style="background:#2e5aa8"></span>
      <span style="background:#1a6fa3"></span>
      <span style="background:#d2452f"></span>
    </div>
  </div>
  <div class="footer-rule"></div>
  <p class="copyright">© 2016 Company Name &nbsp;All right reserved &nbsp;Term of Use</p>
</footer>

</body>
</html>
```